Harrowgate - Pell Corporate PowerPoint Presentation Template

A custom, corporate template that is highly professional, neat/crisp, "serious," and captures/emphasizes the essence of a global, mutli-brand consumer products company that has deep tradition and values family, hard work, performance, innovation, and service to our consumers and retail partners.
The company's roots and headquarters are in Texas. We are a private and family owned since our founding almost 100 years ago. The corporate website is www.hpvcorp-example.com and other branded websites can be accessed from this site.
Our current presentation title page is attached. We believe it to be somewhat stale/out of date and less sophisticated that the image we'd prefer to project. We occasionally add/change logos and will have to adapt the presentation. These presentations must look good printed.
Please contact me with any questions or requests and I will respond very quickly.
Target Market(s)
Corporate Executives
Industry/Entity Type
It Professional
Requirements
Must have
- Sans Serif font (can't select below). Industry is Apparel and Footwear / Consumer Products (can't select below).

```html
<!DOCTYPE html>
<html lang="en">
<head>
<meta charset="utf-8">
<title>Values and Vision – Harrowgate - Pell</title>
<link rel="stylesheet" href="https://fonts.googleapis.com/css2?family=Source+Sans+3:wght@300;400&display=swap">
<style>
  :root {
    --bg: #ffffff;
    --title: #3a3a3a;
    --subtitle: #8a8a8a;
    --tagline: #6b6b6b;
    --accent-red: #d3174b;
    --accent-blue: #1a73b8;
    --body: #b5b5b5;
    --rule: #9a9a9a;
    --on-accent: #ffffff;
  }
  * { box-sizing: border-box; margin: 0; padding: 0; }
  html, body { width: 1200px; height: 675px; overflow: hidden; background: var(--bg); }
  body { font-family: "Source Sans 3", "Source Sans Pro", Arial, sans-serif; }
  .slide { position: relative; width: 1200px; height: 675px; }

  .slide-header { position: absolute; top: 64px; left: 0; width: 100%; text-align: center; }
  .slide-title { font-weight: 300; font-size: 38px; color: var(--title); line-height: 1.1; }
  .slide-subtitle { font-weight: 300; font-size: 17px; color: var(--subtitle); margin-top: 12px; }

  .brand-mark {
    position: absolute; left: 225px; top: 171px;
    width: 174px; height: 174px; border-radius: 50%;
    background: var(--accent-red);
    display: flex; align-items: center; justify-content: center; text-align: center;
  }
  .brand-name { color: var(--on-accent); font-weight: 400; font-size: 22px; line-height: 1.2; padding: 0 20px; }

  .tagline {
    position: absolute; right: 812px; top: 368px;
    text-align: right; font-weight: 300; font-size: 31px; line-height: 36px; color: var(--tagline);
  }

  .divider { position: absolute; left: 481px; top: 228px; width: 1px; height: 300px; background: var(--rule); }

  .vision { position: absolute; left: 557px; top: 222px; width: 505px; }
  .vision-heading { font-weight: 400; font-size: 27px; line-height: 37px; color: var(--accent-blue); }
  .vision-text { font-weight: 300; font-size: 16px; line-height: 29px; color: var(--body); margin-top: 12px; }
  .vision-text + .vision-text { margin-top: 29px; }
</style>
</head>
<body>
  <main class="slide">
    <header class="slide-header">
      <h1 class="slide-title">Values and Vision</h1>
      <p class="slide-subtitle">Put your great subtitle here!</p>
    </header>

    <div class="brand-mark">
      <span class="brand-name">Harrowgate - Pell</span>
    </div>

    <p class="tagline">Exceeding<br>expectations<br>since 1922</p>

    <div class="divider"></div>

    <section class="vision">
      <h2 class="vision-heading">We are a Trusted and<br>Established Company with a new vision.</h2>
      <p class="vision-text">Lorem ipsum dolor sit amet, consectetur adipiscing elit. Aliquam tincidunt ante nec sem congue convallis. Pellentesque vel mauris quis nisl ornare rutrum in id risus. Proin vehicula ut sem et tempus. Interdum et malesuada fames ac ante ipsum primis in faucibus.</p>
      <p class="vision-text">Lorem ipsum dolor sit amet, consectetur adipiscing elit. Aliquam tincidunt ante nec sem congue convallis. Pellentesque vel mauris quis nisl ornare</p>
    </section>
  </main>
</body>
</html>
```